Company Profile for Academic and Study Abroad Services

I am looking for Power Point Design for company Profile . the company is academic and study abroad services. you can visit the website which is www.korvelan.ae . the colour i prefer is Dark Blue + White + Black . you can find all the content for power point and logo and some picture i need you to add it.

Target Market(s)

Students who wants to study abroad. Universities . Learning centre.

Industry/Entity Type

Education

Font styles to use
Serif
Sans Serif

Colors
0555a3
ffffff
000000
aaaaaa

Requirements
Must have
• Must Have Images for each slides.
Nice to have
• infographic. Images related to the study abroad

```html
<!DOCTYPE html>
<html lang="en">
<head>
<meta charset="utf-8">
<title>Korvelan – Company Profile Slides</title>
<link rel="stylesheet" href="https://fonts.googleapis.com/css2?family=Open+Sans:wght@400;600;700&display=swap">
<style>
  :root {
    --board-light: #8d8d8d;
    --board-dark: #5a5a5a;
    --white: #ffffff;
    --royal: #0a0aa0;
    --royal-mid: #1f3fae;
    --royal-soft: #2f5cb8;
    --band-gray: #8e9093;
    --ink-1: #252930;
    --ink-2: #30353d;
    --ink-3: #3d434c;
    --navy-text: #1d2b57;
    --body-ink: #1b1b1b;
  }
  * { box-sizing: border-box; margin: 0; padding: 0; }
  html, body { width: 1200px; height: 1200px; overflow: hidden; }
  body {
    font-family: "Open Sans", sans-serif;
    background: linear-gradient(135deg, var(--board-light) 0%, #6f6f6f 55%, var(--board-dark) 100%);
    position: relative;
  }
  .slide {
    position: absolute;
    width: 475px;
    height: 268px;
    background: var(--white);
    overflow: hidden;
    box-shadow: 4px 8px 14px rgba(0,0,0,0.45);
  }
  .col-left { left: 93px; }
  .col-right { left: 632px; }
  .row-1 { top: 140px; }
  .row-2 { top: 466px; }
  .row-3 { top: 793px; }

  /* shared header */
  .slide-header { position: absolute; left: 0; top: 0; width: 475px; height: 56px; }
  .slide-title {
    position: absolute; left: 14px; top: 9px;
    color: var(--white); font-weight: 700; font-size: 14.5px; letter-spacing: 0.2px;
  }
  .slide-title::after {
    content: ""; display: block; width: 118px; height: 2px; background: var(--white); margin-top: 3px;
  }
  .brand {
    position: absolute; right: 9px; top: 14px;
    display: flex; flex-direction: column; align-items: center; gap: 3px;
  }
  .brand-square { width: 9px; height: 9px; background: var(--navy-text); }
  .brand-name { font-weight: 700; font-size: 8px; color: var(--navy-text); letter-spacing: 0.3px; line-height: 1; }
  .site-url {
    position: absolute; left: 18px; bottom: 12px;
    font-size: 9px; font-weight: 700; color: var(--navy-text);
  }
  .small-copy {
    font-size: 6.3px; font-weight: 700; line-height: 13px; color: var(--body-ink); text-align: center;
  }

  /* cover */
  .cover-photo {
    position: absolute; inset: 0;
    background: linear-gradient(110deg, #9aa38a 0%, #c9b9a6 30%, #3a3a44 55%, #262630 75%, #d8c9c0 100%);
  }
  .cover-brand { position: absolute; left: 16px; top: 12px; display: flex; align-items: center; gap: 4px; }
  .cover-brand .brand-name { color: #1c2550; font-size: 10px; }
  .cover-headline {
    position: absolute; left: 258px; top: 160px;
    color: var(--white); font-weight: 700; font-size: 13px; line-height: 18px;
  }

  /* who we are */
  .step-row { position: absolute; left: 45px; top: 94px; }
  .step-label { font-size: 14px; fill: var(--white); font-family: "Open Sans", sans-serif; }
  .step-copy { position: absolute; top: 176px; width: 118px; }

  /* what we do */
  .service-icon { position: absolute; top: 84px; width: 20px; height: 20px; }
  .service-box {
    position: absolute; top: 107px; width: 120px; height: 49px;
    display: flex; align-items: center; justify-content: center;
    color: var(--white); font-size: 11.5px;
  }
  .service-copy { position: absolute; top: 170px; width: 124px; }

  /* education levels */
  .level-band {
    position: absolute; left: 0; top: 86px; width: 475px; height: 126px; background: var(--royal);
  }
  .level-pattern { position: absolute; right: 0; top: 0; width: 221px; height: 126px; }
  .level-title { position: absolute; left: 24px; top: 8px; color: var(--white); font-size: 18px; font-weight: 400; }
  .level-copy {
    position: absolute; left: 24px; top: 38px; color: var(--white);
    font-size: 10px; font-weight: 700; line-height: 19.5px; width: 205px;
  }

  /* why choose */
  .reason-bar {
    position: absolute; left: 0; top: 83px; width: 378px; height: 24px; background: var(--royal);
    color: var(--white); font-size: 13px; text-align: right; padding-right: 48px; line-height: 24px;
  }
  .reason-col { position: absolute; top: 107px; width: 90px; height: 161px; padding: 11px 8px 6px 10px; color: var(--white); overflow: hidden; }
  .reason-col h3 { font-size: 9.5px; font-weight: 400; margin-bottom: 7px; }
  .reason-col p { font-size: 5.4px; font-weight: 700; line-height: 10px; }
  .magnifier { position: absolute; left: 346px; top: 78px; }

  /* study destination */
  .dest-icon { position: absolute; top: 81px; width: 37px; height: 37px; background: var(--ink-1); }
  .dest-icon svg { position: absolute; left: 9px; top: 9px; width: 19px; height: 19px; }
  .dest-copy {
    position: absolute; left: 26px; top: 131px; width: 180px;
    font-size: 8.3px; font-weight: 700; line-height: 14px; color: var(--body-ink);
  }
  .option-row { position: absolute; left: 237px; width: 201px; height: 37px; display: flex; }
  .option-letter {
    width: 41px; background: var(--ink-3); color: var(--white);
    font-size: 17px; display: flex; align-items: center; justify-content: center;
  }
  .option-text {
    flex: 1; background: var(--ink-1); color: var(--white);
    font-size: 5.6px; font-weight: 700; line-height: 9px; padding: 10px 6px 0 6px;
  }
</style>
</head>
<body>

<!-- Cover -->
<section class="slide col-left row-1">
  <div class="cover-photo" role="img" aria-label="Photo of smiling graduates in caps and gowns holding diplomas"></div>
  <svg width="475" height="268" style="position:absolute;left:0;top:0">
    <defs>
      <linearGradient id="coverGrad" x1="0" y1="0" x2="1" y2="1">
        <stop offset="0" stop-color="#2a4fb4"/>
        <stop offset="1" stop-color="#0a0aa0"/>
      </linearGradient>
      <linearGradient id="hdrGrad" x1="0" y1="0" x2="1" y2="1">
        <stop offset="0" stop-color="#2f5cb8"/><stop offset="1" stop-color="#0a0aa0"/>
      </linearGradient>
    </defs>
    <polygon points="324,0 475,0 475,268 0,268 0,238 235,238 324,150" fill="var(--royal)"/>
    <polygon points="324,0 475,0 475,238 235,238 324,150" fill="url(#coverGrad)" role="img" aria-label="Blue geometric triangle pattern"/>
  </svg>
  <div class="cover-brand"><span class="brand-square"></span><span class="brand-name">KORVELAN</span></div>
  <div class="cover-headline">KORVELAN<br>Universities<br>Entrance Services</div>
</section>

<!-- Who we are -->
<section class="slide col-right row-1">
  <svg class="slide-header" viewBox="0 0 475 56">
    <rect x="0" y="0" width="408" height="43" fill="var(--band-gray)"/>
    <polygon points="290,0 408,0 368,56 250,56" fill="url(#hdrGrad)" role="img" aria-label="Blue geometric triangle pattern"/>
  </svg>
  <h2 class="slide-title">WHO WE ARE</h2>
  <div class="brand"><span class="brand-square"></span><span class="brand-name">KORVELAN</span></div>
  <svg class="step-row" width="390" height="68" viewBox="0 0 390 68">
    <polygon points="0,0 118,0 140,34 118,68 0,68 20,34" fill="var(--ink-1)"/>
    <polygon points="122,0 240,0 262,34 240,68 122,68 142,34" fill="var(--ink-2)"/>
    <polygon points="245,0 363,0 385,34 363,68 245,68 265,34" fill="var(--ink-3)"/>
    <text class="step-label" x="44" y="39">STEP 1</text>
    <text class="step-label" x="166" y="39">STEP 2</text>
    <text class="step-label" x="289" y="39">STEP 3</text>
  </svg>
  <p class="small-copy step-copy" style="left:56px">Lorem ipsum dolor sit amet, enim dolore mucius ei eam. Esse aliquip nonumes et eos. Eripuit deserunt argumentum id eum, nulla nonumes.</p>
  <p class="small-copy step-copy" style="left:178px">Lorem ipsum dolor sit amet, enim dolore mucius ei eam. Esse aliquip nonumes et eos. Eripuit deserunt argumentum id eum, nulla nonumes.</p>
  <p class="small-copy step-copy" style="left:301px">Lorem ipsum dolor sit amet, enim dolore mucius ei eam. Esse aliquip nonumes et eos. Eripuit deserunt argumentum id eum, nulla nonumes.</p>
  <span class="site-url">www.korvelan.ae</span>
</section>

<!-- What we do -->
<section class="slide col-left row-2">
  <svg class="slide-header" viewBox="0 0 475 56">
    <rect x="0" y="0" width="408" height="43" fill="var(--band-gray)"/>
    <polygon points="290,0 408,0 368,56 250,56" fill="url(#hdrGrad)" role="img" aria-label="Blue geometric triangle pattern"/>
  </svg>
  <h2 class="slide-title">WHAT WE DO</h2>
  <div class="brand"><span class="brand-square"></span><span class="brand-name">KORVELAN</span></div>
  <svg class="service-icon" style="left:90px" viewBox="0 0 20 20"><rect x="2" y="9" width="2.5" height="9" fill="var(--ink-1)"/><rect x="6" y="5" width="2.5" height="13" fill="var(--ink-1)"/><rect x="10" y="2" width="2.5" height="16" fill="var(--ink-1)"/><rect x="14" y="7" width="2.5" height="11" fill="var(--ink-1)"/><rect x="0" y="18" width="20" height="1.5" fill="var(--ink-1)"/></svg>
  <svg class="service-icon" style="left:227px" viewBox="0 0 20 20"><polygon points="10,1 20,10 17,10 17,19 12,19 12,13 8,13 8,19 3,19 3,10 0,10" fill="var(--ink-1)"/></svg>
  <svg class="service-icon" style="left:365px" viewBox="0 0 20 20"><circle cx="10" cy="6" r="5" fill="var(--ink-1)"/><path d="M1 20 Q1 11 10 11 Q19 11 19 20 Z" fill="var(--ink-1)"/></svg>
  <div class="service-box" style="left:40px;background:var(--ink-1)">Lorem ipsum</div>
  <div class="service-box" style="left:177px;background:var(--ink-2)">Lorem ipsum</div>
  <div class="service-box" style="left:315px;background:var(--ink-2)">Lorem ipsum</div>
  <p class="small-copy service-copy" style="left:38px">Lorem ipsum dolor sit amet, enim dolore mucius ei eam. Esse aliquip nonumes et eos. Eripuit deserunt argumentum id eum, nulla nonumes.</p>
  <p class="small-copy service-copy" style="left:175px">Lorem ipsum dolor sit amet, enim dolore mucius ei eam. Esse aliquip nonumes et eos. Eripuit deserunt argumentum id eum, nulla nonumes.</p>
  <p class="small-copy service-copy" style="left:313px">Lorem ipsum dolor sit amet, enim dolore mucius ei eam. Esse aliquip nonumes et eos. Eripuit deserunt argumentum id eum, nulla nonumes.</p>
  <span class="site-url">www.korvelan.ae</span>
</section>

<!-- Education levels -->
<section class="slide col-right row-2">
  <svg class="slide-header" viewBox="0 0 475 56">
    <rect x="0" y="0" width="408" height="43" fill="var(--band-gray)"/>
    <polygon points="290,0 408,0 368,56 250,56" fill="url(#hdrGrad)" role="img" aria-label="Blue geometric triangle pattern"/>
  </svg>
  <h2 class="slide-title">EDUCATION LEVELS</h2>
  <div class="brand"><span class="brand-square"></span><span class="brand-name">KORVELAN</span></div>
  <div class="level-band">
    <div class="level-pattern" role="img" aria-label="Blue geometric triangle pattern" style="background:linear-gradient(120deg, var(--royal) 0%, #1b3aa8 45%, #2a56b4 100%)"></div>
    <h3 class="level-title">Lorem ipsum</h3>
    <p class="level-copy">Lorem ipsum dolor sit amet, enim dolore mucius ei eam. Esse aliquip nonumes et eos. Eripuit deserunt argumentum id eum, nulla nonumes.</p>
  </div>
  <span class="site-url">www.korvelan.ae</span>
</section>

<!-- Why choose -->
<section class="slide col-left row-3">
  <svg class="slide-header" viewBox="0 0 475 56">
    <rect x="0" y="0" width="408" height="43" fill="var(--band-gray)"/>
    <polygon points="290,0 408,0 368,56 250,56" fill="url(#hdrGrad)" role="img" aria-label="Blue geometric triangle pattern"/>
  </svg>
  <h2 class="slide-title">WHY CHOOSE KORVELAN</h2>
  <div class="brand"><span class="brand-square"></span><span class="brand-name">KORVELAN</span></div>
  <div class="reason-bar">Lorem Ipsum</div>
  <div class="reason-col" style="left:0;background:var(--ink-1)"><h3>Lorem ipsum</h3><p>Lorem ipsum dolor sit amet, enim dolore mucius ei eam. Esse aliquip nonumes et eos. Eripuit deserunt argumentum id.</p><p>Lorem ipsum dolor sit amet, enim dolore mucius ei eam. Esse aliquip nonumes et eos. Eripuit deserunt argumentum id.</p></div>
  <div class="reason-col" style="left:90px;background:var(--ink-2)"><h3>Lorem ipsum</h3><p>Lorem ipsum dolor sit amet, enim dolore mucius ei eam. Esse aliquip nonumes et eos. Eripuit deserunt argumentum id.</p><p>Lorem ipsum dolor sit amet, enim dolore mucius ei eam. Esse aliquip nonumes et eos. Eripuit deserunt argumentum id.</p></div>
  <div class="reason-col" style="left:180px;background:var(--ink-3)"><h3>Lorem ipsum</h3><p>Lorem ipsum dolor sit amet, enim dolore mucius ei eam. Esse aliquip nonumes et eos. Eripuit deserunt argumentum id.</p><p>Lorem ipsum dolor sit amet, enim dolore mucius ei eam. Esse aliquip nonumes et eos. Eripuit deserunt argumentum id.</p></div>
  <svg class="magnifier" width="104" height="170" viewBox="0 0 104 170">
    <circle cx="52" cy="52" r="44" fill="var(--royal-mid)" stroke="var(--ink-3)" stroke-width="10"/>
    <rect x="44" y="99" width="16" height="18" fill="var(--ink-3)"/>
    <rect x="44" y="125" width="16" height="27" fill="var(--ink-3)"/>
  </svg>
</section>

<!-- Study destination -->
<section class="slide col-right row-3">
  <svg class="slide-header" viewBox="0 0 475 56">
    <rect x="0" y="0" width="408" height="43" fill="var(--band-gray)"/>
    <polygon points="290,0 408,0 368,56 250,56" fill="url(#hdrGrad)" role="img" aria-label="Blue geometric triangle pattern"/>
  </svg>
  <h2 class="slide-title">STUDY DESTINATION</h2>
  <div class="brand"><span class="brand-square"></span><span class="brand-name">KORVELAN</span></div>
  <div class="dest-icon" style="left:26px"><svg viewBox="0 0 20 20"><rect x="2" y="9" width="2.5" height="9" fill="#fff"/><rect x="6" y="5" width="2.5" height="13" fill="#fff"/><rect x="10" y="2" width="2.5" height="16" fill="#fff"/><rect x="14" y="7" width="2.5" height="11" fill="#fff"/><rect x="0" y="18" width="20" height="1.5" fill="#fff"/></svg></div>
  <div class="dest-icon" style="left:81px"><svg viewBox="0 0 20 20"><polygon points="10,1 20,10 17,10 17,19 12,19 12,13 8,13 8,19 3,19 3,10 0,10" fill="#fff"/></svg></div>
  <div class="dest-icon" style="left:136px"><svg viewBox="0 0 20 20"><circle cx="10" cy="6" r="5" fill="#fff"/><path d="M1 20 Q1 11 10 11 Q19 11 19 20 Z" fill="#fff"/></svg></div>
  <p class="dest-copy">Lorem ipsum dolor sit amet, enim dolore mucius ei eam. Esse aliquip nonumes et eos. Eripuit deserunt argumentum id eum, nulla nonumes. Lorem ipsum dolor sit amet, enim dolore mucius ei eam. Esse aliquip nonumes et eos. Eripuit deserunt</p>
  <div class="option-row" style="top:82px"><span class="option-letter">A</span><span class="option-text">Lorem ipsum dolor sit amet, enim dolore mucius ei eam. Esse aliquip noscumes et eos. Eripuit deserunt.</span></div>
  <div class="option-row" style="top:142px"><span class="option-letter" style="background:var(--ink-1)">B</span><span class="option-text">Lorem ipsum dolor sit amet, enim dolore mucius ei eam. Esse aliquip noscumes et eos. Eripuit deserunt.</span></div>
  <div class="option-row" style="top:202px"><span class="option-letter">C</span><span class="option-text" style="background:var(--ink-3)">Lorem ipsum dolor sit amet, enim dolore mucius ei eam. Esse aliquip noscumes et eos. Eripuit deserunt.</span></div>
  <span class="site-url">www.korvelan.ae</span>
</section>

</body>
</html>
```